2016 Spring tune up

We sell automatic pool covers. We need a postcard design for a mailer to be sent to our customers about a yearly tune up , also offering a discount for a fabric replacement for their automatic pool cover system. The attached information and pictures should be included on the postcard. We would like to see designs that include the colors in our address label

Target Market(s)

Current Automatic Pool Cover Owners

Requirements
Must have
• www.mdrvk.com
• Contact info-service@mdrvk.com
• Attached images and documents
Nice to have
• Color match to our attached logo
Should not have
• Should not have pictures with pools without covers.

```html
<!DOCTYPE html>
<html lang="en">
<head>
<meta charset="utf-8">
<title>Spring Tune Up Postcard</title>
<link href="https://fonts.googleapis.com/css2?family=Montserrat:wght@400;500;600;700;800&display=swap" rel="stylesheet">
<style>
:root{
  --page:#2e2f31;
  --blue:#1b76c4;
  --blue-deep:#145e9f;
  --sky:#8ed2f3;
  --sky-pale:#b5e2f7;
  --band:#4f9fdc;
  --grey:#4e5054;
  --white:#ffffff;
  --line:#d9dde2;
  --stamp:#eceef0;
  --ink:#0f4f86;
}
*{box-sizing:border-box;margin:0;padding:0}
html,body{width:928px;height:1200px;overflow:hidden}
body{background:var(--page);font-family:"Montserrat",Arial,sans-serif;color:var(--white);position:relative}
.card{position:absolute;left:84px;width:760px;height:563px;overflow:hidden}
.card--front{top:24px;background:var(--blue)}
.card--back{top:613px;background:var(--white)}

/* front */
.photo{position:absolute;inset:0;clip-path:polygon(0 0,448px 0,298px 563px,0 563px);
  background:linear-gradient(180deg,#3f86c0 0%,#6fb4df 35%,#2f7fa8 52%,#8a6048 70%,#5f4636 100%)}
.photo-edge{position:absolute;inset:0;background:var(--sky);
  clip-path:polygon(448px 0,472px 0,322px 563px,298px 563px)}
.offer-veil{position:absolute;inset:0;background:linear-gradient(180deg,rgba(27,118,196,.92),rgba(27,118,196,.55));
  clip-path:polygon(0 0,448px 0,400px 182px,0 182px)}
.offers{position:absolute;left:42px;top:24px;width:360px;text-transform:uppercase}
.offers p{font-size:11px;font-weight:700;line-height:1.25}
.offers .price{font-size:22px;font-weight:800;line-height:1.1;margin-bottom:8px}
.prepay{position:absolute;left:77px;top:222px;width:162px;height:162px;border-radius:50%;
  background:var(--sky-pale);border:5px solid var(--white);color:var(--ink);
  display:flex;flex-direction:column;justify-content:center;align-items:center;text-align:center;padding:14px}
.prepay p{font-size:9px;line-height:1.35}
.prepay strong{font-weight:700}
.prepay .call{font-size:8.5px;font-weight:700;margin-top:8px;text-transform:uppercase}
.brand{position:absolute;left:466px;top:26px;width:260px;font-size:21px;font-weight:800;line-height:1.1;text-transform:uppercase}
.details{position:absolute;left:462px;top:102px;width:282px}
.detail{border-bottom:1.5px solid var(--white);padding:6px 0 8px}
.detail:last-child{border-bottom:none}
.detail h3{font-size:9.5px;font-weight:700;text-transform:uppercase;margin-bottom:2px}
.detail p{font-size:9px;line-height:1.3}
.special{position:absolute;inset:0;background:var(--grey);clip-path:polygon(353px 358px,760px 358px,760px 436px,333px 436px)}
.special-text{position:absolute;left:380px;top:370px;width:370px;font-size:16px;font-weight:500;line-height:1.2;text-transform:uppercase}
.special-text b{font-weight:800}
.contact{position:absolute;left:384px;top:454px;font-size:11px;font-weight:700;text-transform:uppercase}
.contact dl{display:grid;grid-template-columns:64px auto;row-gap:6px}
.contact .web{margin-top:10px}

/* back */
.panel{position:absolute;left:0;top:0;width:368px;height:466px;background:var(--blue)}
.panel .brand{left:30px;top:26px;width:310px;text-align:center}
.address{position:absolute;left:0;top:100px;width:368px;text-align:center;font-size:10px;font-weight:600;line-height:1.4}
.promo{position:absolute;left:0;top:160px;width:368px;height:114px;background:var(--band);
  display:flex;align-items:center;justify-content:center;text-align:center;font-size:19px;font-weight:700;line-height:1.3;text-transform:uppercase}
.seal{position:absolute;left:114px;top:296px;width:140px;height:140px;border-radius:50%;
  background:radial-gradient(circle,#e9e9e9 0 52%,#c7a24a 53% 62%,#8f9296 63%)}
.stamp{position:absolute;left:595px;top:32px;width:109px;height:123px;background:var(--stamp)}
.address-lines{position:absolute;left:398px;top:266px;width:286px}
.address-lines span{display:block;height:1.5px;background:var(--line);margin-bottom:44px}
</style>
</head>
<body>

<section class="card card--front">
  <div class="photo" role="img" aria-label="Photo of a covered backyard pool with wooden deck overlooking a lake"></div>
  <div class="offer-veil"></div>
  <div class="photo-edge"></div>

  <div class="offers">
    <p>We are offering our yearly tune up<br>specials basic cover cleaning</p>
    <p class="price">Starting at $290.00</p>
    <p>Mechanical tune up</p>
    <p class="price">Starting at $330.00</p>
    <p>Deluxe tune up</p>
    <p class="price">Starting at $495.00</p>
  </div>

  <div class="prepay">
    <p>Prepay fabric replacement or spring tune up by <strong>April 15, 2016</strong> and receive a 20% discount or by <strong>April 30, 2016</strong> and receive a 10% discount. (Vanishing stone lids extra)</p>
    <p class="call">Please call for details</p>
  </div>

  <h1 class="brand">Northshore<br>Automatic Pool Covers</h1>

  <div class="details">
    <div class="detail">
      <h3>Basic cover cleaning includes</h3>
      <p>Cleaning of the top of the cover only (up to 2 hours of labor included). (Does not include adjustments/lubrication)</p>
    </div>
    <div class="detail">
      <h3>Mechanical tune up includes</h3>
      <p>Removal of debris and cleaning of recessed housing or bench/enclosure, lubrication, inspection of all moving parts, tightening track, and making adjustments for proper operation (up to 2 hours of labor included). Replacement of End Casting Pulleys to help prevent premature rope breakage. (Does not include cleaning of fabric)</p>
    </div>
    <div class="detail">
      <h3>Deluxe tune up includes</h3>
      <p>All of the services provided in the basic cover cleaning and Mechanical tune up plus: Replacement of gliders (on under track units only), guides and shear bolt or pin. (up to 3 hours of labor included)</p>
    </div>
  </div>

  <div class="special"></div>
  <p class="special-text">20% off fabric replacement<br>and spring tune up specials<br><b>(Call for details)</b></p>

  <div class="contact">
    <dl>
      <dt>Phone</dt><dd>: 800-555-0142</dd>
      <dt>Fax</dt><dd>: 231-555-0187</dd>
      <dt>E-mail</dt><dd>: info-service@mdrvk.com</dd>
    </dl>
    <p class="web">www.mdrvk.com</p>
  </div>
</section>

<section class="card card--back">
  <div class="panel">
    <h2 class="brand">Northshore<br>Automatic Pool Covers</h2>
    <p class="address">2850 N. Harbor Ave.<br>Lakeview, MI 49000</p>
    <p class="promo">20% off<br>fabric replacement<br>and<br>spring tune up!!!</p>
    <div class="seal" role="img" aria-label="Anniversary seal"></div>
  </div>
  <div class="stamp"></div>
  <div class="address-lines"><span></span><span></span><span></span><span></span></div>
</section>

</body>
</html>
```